Electrical Contracting business card design

We need a simple business card design for an Electrical Contracting business. A simple design would be appreciated
This company has 2 directors so on one it would have Dale Morrow & another with Shane Morrow.
Updates

Project Deadline Extended
Reason: Hello A few designers have asked for a logo unfortunately we don't have one so have extended deadline to see who can help us out with this. CHEERS

Project Deadline Extended
Reason: Waiting for business partner to return from xmas break. cheers

Industry/Entity Type

Business

Contact Information for Business Card

Quolvin Electrical Services P/L
REC: 63417
Residential Commercial Industrial
Service-Repairs-Renovations-Installations-Telephone-Data
Dale Morrow-Ph: 0437 612 388
Email: dale@quolvinelectrical.com.au

Requirements
Should not have
• The design should not have any electrical appliances in it ie: power-points, leads, houses etc.

```html
<!DOCTYPE html>
<html lang="en">
<head>
<meta charset="UTF-8">
<title>Quolvin Electrical Services – Business Card</title>
<link rel="stylesheet" href="https://fonts.googleapis.com/css2?family=Bebas+Neue&family=Josefin+Sans:wght@400&display=swap">
<style>
  :root {
    --page-bg: #ffffff;
    --card-bg: #111111;
    --accent: #f7901e;
  }
  html, body {
    margin: 0;
    padding: 0;
    width: 1200px;
    height: 1000px;
    overflow: hidden;
    background: var(--page-bg);
  }
  .canvas {
    position: relative;
    width: 1200px;
    height: 1000px;
  }
  .card {
    position: absolute;
    background: var(--card-bg);
  }
  .card--front {
    left: 24px;
    top: 15px;
    width: 752px;
    height: 464px;
  }
  .card--back {
    left: 422px;
    top: 517px;
    width: 757px;
    height: 466px;
  }
  .company-name {
    position: absolute;
    margin: 0;
    font-family: "Bebas Neue", "Arial Narrow", sans-serif;
    font-weight: 400;
    color: var(--accent);
    white-space: nowrap;
    line-height: 1;
    letter-spacing: 0.3px;
    transform: translateX(-50%);
  }
  .card--front .company-name {
    left: 380px;
    top: 226px;
    font-size: 33px;
  }
  .card--back .company-name {
    left: 215px;
    top: 228px;
    font-size: 28px;
  }
  .divider {
    position: absolute;
    left: 428px;
    top: 150px;
    width: 3px;
    height: 183px;
    background: var(--accent);
  }
  .contact {
    position: absolute;
    left: 511px;
    top: 143px;
    font-family: "Josefin Sans", "Century Gothic", sans-serif;
    color: var(--accent);
    white-space: nowrap;
  }
  .contact p {
    margin: 0;
  }
  .contact__name {
    font-size: 22px;
    line-height: 26px;
  }
  .contact__role {
    font-size: 13px;
    line-height: 17px;
    margin-top: 1px !important;
  }
  .contact__phone {
    font-size: 12px;
    line-height: 17px;
  }
  .contact__email {
    font-size: 10px;
    line-height: 18px;
  }
  .contact__licence {
    font-size: 12px;
    line-height: 17px;
  }
  .services {
    list-style: none;
    margin: 0;
    padding: 0;
    font-size: 10px;
    line-height: 13.7px;
  }
</style>
</head>
<body>
  <main class="canvas">
    <section class="card card--front" aria-label="Card front">
      <h1 class="company-name">Quolvin Electrical Services</h1>
    </section>

    <section class="card card--back" aria-label="Card back">
      <h2 class="company-name">Quolvin Electrical Services</h2>
      <div class="divider"></div>
      <div class="contact">
        <p class="contact__name">Shane Morrow</p>
        <p class="contact__role">Directors</p>
        <p class="contact__phone">0437 612 388</p>
        <p class="contact__email">Email: dale@quolvinelectrical.com.au</p>
        <p class="contact__licence">P/L REC: 63417</p>
        <ul class="services">
          <li>Residential Commercial</li>
          <li>IndustrialService</li>
          <li>Repairs</li>
          <li>Renovations</li>
          <li>Installations</li>
          <li>Telephone</li>
          <li>Data</li>
        </ul>
      </div>
    </section>
  </main>
</body>
</html>
```